Company Profile for Consulting Comany

Need Company profile to be designed in a professional way.

for inspiring :-
https://www.vimolia.net/gallery/5307462/COMPANY-PROFILE
https://www.vimolia.net/gallery/20934617/Biotech-Product-Catalog-No1-(Laminar-Air-Flow)
https://www.vimolia.net/gallery/38720954/RKT-Tramvale-Company-Profile-2014-(RKT-Rebrand-part-2)

Target Market(s)

Corporate

Industry/Entity Type

It Company

Font styles to use
Sans Serif

Requirements
Must have
• Landscape A4 size
• Must go with the logo branding
• Must Have Visual Identity is the most important
• Must Have mpty spaces

```html
<!DOCTYPE html>
<html lang="en">
<head>
<meta charset="utf-8">
<title>Stride Works — Company Profile Spreads</title>
<link rel="stylesheet" href="https://fonts.googleapis.com/css2?family=Montserrat:wght@300;600;700;800&family=Open+Sans:wght@400;600;700&display=swap">
<style>
:root{
  --stage:#666666;
  --paper:#ffffff;
  --ink:#111111;
  --black:#000000;
  --panel:#a8a8a8;
  --panel-light:#c4c4c4;
  --teal:#29b5e8;
  --fine:#222222;
  --fine-on-dark:#d6d6d6;
  --mark:#3d3d3d;
  --cell:#f1f1f1;
}
*{margin:0;padding:0;box-sizing:border-box}
html,body{width:1200px;height:686px;overflow:hidden;background:var(--stage)}
body{position:relative;font-family:"Open Sans",Arial,sans-serif}
.page{position:absolute;width:266px;height:187px;background:var(--paper);overflow:hidden}
.page.dark{background:var(--black)}
.band{position:absolute;left:0;width:100%;background:var(--black)}
.panel{position:absolute;background:var(--panel)}
.title{position:absolute;font-family:"Montserrat",Arial,sans-serif;font-weight:800;color:var(--ink);line-height:.92;letter-spacing:-.2px;white-space:nowrap}
.title.light{color:#fff}
.fine{position:absolute;font-size:3.6px;line-height:4.6px;color:var(--fine)}
.fine.on-dark{color:var(--fine-on-dark)}
.fine b{display:block;font-weight:700;font-size:3.8px;color:var(--ink);margin-bottom:.6px;letter-spacing:.1px}
.fine.on-dark b{color:#fff}
.fine p{margin-bottom:3px}
.folio{position:absolute;bottom:7px;font-size:3.6px;color:#777}
.brand{position:absolute;display:flex;align-items:center;gap:4px;font-family:"Montserrat",Arial,sans-serif;font-weight:700;color:var(--teal);line-height:1}
.brand .sq{border:1.6px solid var(--teal);flex:none}
.toc{list-style:none}
.toc li{display:flex;justify-content:space-between}
.logo-grid{position:absolute;display:grid;gap:4px}
.logo-cell{display:flex;align-items:center;gap:3px;background:var(--cell);padding:0 4px;height:100%;font-family:"Montserrat",Arial,sans-serif;font-weight:600;color:var(--mark);white-space:nowrap;overflow:hidden}
.logo-cell .sq{width:6px;height:6px;background:var(--mark);flex:none}
.portrait{position:absolute;background:linear-gradient(#d4d4d4,#7a7a7a)}
</style>
</head>
<body>

<!-- Row 1 -->
<section class="page back-cover" style="left:56px;top:53px">
  <div class="band" style="top:73px;height:92px"></div>
  <div class="brand" style="left:30px;top:112px;font-size:6.5px"><span class="sq" style="width:12px;height:12px"></span>Stride Works</div>
  <div class="fine on-dark" style="left:82px;top:108px;width:72px"><b>DUBAI</b>PO Box 55012, Dubai, UAE<br>21st Floor, Harbour Tower<br>T +971 4 555 0142<br>hello@strideworks.example</div>
  <div class="fine on-dark" style="left:162px;top:108px;width:80px"><b>KHOBAR</b>PO Box 31952, Khobar, KSA<br>King Road, Office 18<br>T +966 13 555 0177<br>ksa@strideworks.example</div>
</section>

<section class="page dark front-cover" style="left:330px;top:53px">
  <div class="title" style="left:0;width:100%;top:62px;text-align:center;font-size:8.5px;color:var(--teal);font-weight:700">WE CAN HELP YOU TO</div>
  <div class="title light" style="left:0;width:100%;top:73px;text-align:center;font-size:10px;font-weight:300">MAKE CHANGE HAPPEN</div>
  <div class="brand" style="left:76px;top:98px;font-size:13px"><span class="sq" style="width:30px;height:26px"></span><span>Stride Works<span style="display:block;font-size:4.5px;font-weight:300;margin-top:2px">A Step Toward Progress</span></span></div>
</section>

<section class="page contents" style="left:605px;top:53px">
  <div class="panel" style="left:143px;top:68px;width:100px;height:119px"></div>
  <div class="title" style="left:141px;top:49px;font-size:7px">TABLE OF</div>
  <div class="title" style="left:141px;top:55px;font-size:16px">CONTENTS</div>
  <ul class="fine toc" style="left:149px;top:72px;width:88px;font-size:3.5px;line-height:4.5px">
    <li>Who we are<span>02</span></li><li>&nbsp;Executive Summary<span>02</span></li><li>&nbsp;Vision and Mission<span>02</span></li><li>&nbsp;Values<span>02</span></li><li>Why Stride Works<span>03</span></li><li>What we do<span>04</span></li><li>&nbsp;HR &amp; OD Consultation<span>04</span></li><li>&nbsp;Professional Training<span>04</span></li><li>&nbsp;Talent Assessment<span>05</span></li><li>&nbsp;HR Solutions<span>05</span></li><li>Partnership<span>06</span></li><li>&nbsp;Orvena Associates<span>06</span></li><li>&nbsp;Harlow Pemberton<span>06</span></li><li>&nbsp;Tidemark<span>06</span></li><li>&nbsp;Corvina Consulting<span>06</span></li><li>Our Team<span>07</span></li><li>&nbsp;Samir Halabi<span>07</span></li><li>&nbsp;Karim Nassar<span>07</span></li><li>&nbsp;Fahad Rashed<span>08</span></li><li>&nbsp;Tarek Mansour<span>08</span></li><li>Certifications<span>09</span></li><li>Our Clients<span>10</span></li><li>Contact Us<span>11</span></li>
  </ul>
</section>

<section class="page who" style="left:879px;top:53px">
  <div class="band" style="top:63px;height:78px"></div>
  <div class="panel" style="left:43px;top:55px;width:100px;height:132px"></div>
  <div class="title" style="left:45px;top:42px;font-size:12px">WHO WE ARE?</div>
  <div class="fine" style="left:47px;top:60px;width:92px">
    <p><b>EXECUTIVE SUMMARY</b>Stride Works is a regional HR and OD firm that helps organisations grow people, build strong teams and manage change with clear plans and tested tools across the Gulf.</p>
    <p><b>VISION</b>To be the first choice partner for people and change work in the region.</p>
    <p><b>MISSION</b>We deliver practical solutions that raise the value of people, shape culture and help leaders steer change with care.<br>• To build trust with every client<br>• To grow lasting partnerships<br>• To bring new ideas through learning</p>
  </div>
  <div class="fine on-dark" style="left:152px;top:80px;width:100px"><b>VALUES</b>• INTEGRITY: we act with honesty in all work<br>• RESPECT: we value every person and view<br>• ACCOUNTABILITY: we own our results<br>• EXCELLENCE: we keep raising the bar<br>• QUALITY: we hold strict standards<br>• AFFORDABILITY: fair value for each client</div>
  <div class="folio" style="right:8px">02</div>
</section>

<!-- Row 2 -->
<section class="page why" style="left:56px;top:249px">
  <div class="band" style="top:72px;height:79px"></div>
  <div class="panel" style="left:44px;top:58px;width:100px;height:129px"></div>
  <div class="title" style="left:46px;top:32px;font-size:12px">WHY STRIDE<br>WORKS?</div>
  <div class="fine" style="left:48px;top:62px;width:92px">
    <p><b>SUCCESS</b>We have a proven record of results with leading firms across the region over many years of steady work.</p>
    <p><b>TARGETING</b>We listen first, study the need and build the right plan to meet each goal with care and precision.</p>
    <p><b>SUPERIOR WORKFORCE</b>Our team of certified experts brings deep skill, strong methods and real care to every project we lead, from the first meeting to the final review.</p>
  </div>
  <div class="fine on-dark" style="left:152px;top:96px;width:104px">
    <p><b>FLEXIBLE MULTICHANNEL ABILITIES</b>Our reach spans sectors and regions so we adapt to every setting.</p>
    <p><b>COST EFFECTIVENESS</b>Change done right at a fair and clear price.</p>
  </div>
  <div class="folio" style="left:8px">03</div>
</section>

<section class="page what" style="left:330px;top:249px">
  <div class="band" style="top:72px;height:79px"></div>
  <div class="panel" style="left:127px;top:0;width:139px;height:151px"></div>
  <div class="fine" style="left:133px;top:36px;width:126px">
    <p><b>PROFESSIONAL TRAINING</b>Our training is built on real needs and helps people gain the skills and mindset to perform at their best.</p>
    <p><b>IN HOUSE CUSTOM TRAINING</b>We shape each course around your teams, goals and culture for lasting impact.</p>
    <p><b>PROFESSIONAL QUALIFICATIONS</b>We offer recognised programmes that grow careers and lift the standard of practice in your firm.</p>
  </div>
  <div class="title" style="left:133px;top:117px;font-size:11px">WHAT WE DO?</div>
  <div class="fine on-dark" style="left:28px;top:78px;width:94px"><b>HR &amp; OD CONSULTATION</b>Our team works with leaders to design structures and systems that fit the way the business runs.<br>• HR strategy review<br>• Organisation design<br>• Talent management<br>• Change management<br>• Pay and benefits<br>• Coaching and mentoring</div>
  <div class="folio" style="right:8px">04</div>
</section>

<section class="page assess" style="left:605px;top:249px">
  <div class="band" style="top:72px;height:79px"></div>
  <div class="panel" style="left:45px;top:63px;width:100px;height:124px"></div>
  <div class="fine" style="left:49px;top:67px;width:92px">
    <p><b>TALENT ASSESSMENT</b>We use tested tools to measure skills, style and potential so you can place the right people in the right roles.</p>
    <p><b>TALENT MANAGEMENT</b>We help you plan careers, build strong pipelines and keep key people engaged and ready for growth in the business.</p>
    <p>Each review ends with a clear report and an action plan your leaders can use right away.</p>
  </div>
  <div class="fine on-dark" style="left:153px;top:86px;width:100px"><b>HR SOLUTIONS</b>We take on HR tasks so your team can focus on core work.<br>• Employee relations<br>• Payroll and HR records<br>• Recruiting and hiring<br>• Policies and rules<br>• Performance reviews</div>
  <div class="folio" style="left:8px">05</div>
</section>

<section class="page partners" style="left:879px;top:249px">
  <div class="title" style="left:17px;top:52px;font-size:11px">SUCCESS<br>PARTNERSHIP</div>
  <div class="panel" style="left:15px;top:84px;width:251px;height:103px"></div>
  <div class="logo-grid" style="left:19px;top:87px;width:243px;height:11px;grid-template-columns:repeat(5,1fr);font-size:4.6px">
    <div class="logo-cell"><span class="sq"></span>Orvena</div>
    <div class="logo-cell"><span class="sq"></span>Harlow</div>
    <div class="logo-cell"><span class="sq"></span>Tidemark</div>
    <div class="logo-cell"><span class="sq"></span>Novatalent</div>
    <div class="logo-cell"><span class="sq"></span>Corvina</div>
  </div>
  <div class="fine" style="left:19px;top:103px;width:46px;font-size:3.3px;line-height:4.3px"><b>ORVENA ASSOCIATES</b>A global leader in change and project work with many years in the field and clients in every sector.</div>
  <div class="fine" style="left:68px;top:103px;width:46px;font-size:3.3px;line-height:4.3px"><b>HARLOW PEMBERTON</b>A trusted name in learning and people growth across many markets and industries.</div>
  <div class="fine" style="left:117px;top:103px;width:46px;font-size:3.3px;line-height:4.3px"><b>TIDEMARK</b>A firm that builds smart tools for hiring, skill review and fair selection of staff.</div>
  <div class="fine" style="left:166px;top:103px;width:46px;font-size:3.3px;line-height:4.3px"><b>NOVATALENT</b>An expert in talent review and career plans for large and growing teams.</div>
  <div class="fine" style="left:215px;top:103px;width:46px;font-size:3.3px;line-height:4.3px"><b>CORVINA</b>A partner in reward, role design and leader growth programmes.</div>
  <div class="folio" style="right:8px">06</div>
</section>

<!-- Row 3 -->
<section class="page dark team" style="left:56px;top:446px">
  <div class="title light" style="left:0;width:100%;top:36px;text-align:center;font-size:13px;font-weight:700">OUR TEAM</div>
  <div class="portrait" role="img" aria-label="Portrait photo of Samir Halabi" style="left:98px;top:66px;width:22px;height:22px"></div>
  <div class="portrait" role="img" aria-label="Portrait photo of Karim Nassar" style="left:134px;top:66px;width:22px;height:22px"></div>
  <div class="fine on-dark" style="left:60px;top:92px;width:66px;text-align:center"><b>SAMIR HALABI</b>Consulting Manager<br><br>Certified HR expert with more than ten years of work in OD, training and talent across the region and beyond.</div>
  <div class="fine on-dark" style="left:134px;top:92px;width:68px"><b>KARIM NASSAR</b>Senior Consultant<br><br>Certified trainer with broad skill in change, assessment and leader growth for large firms in many sectors.</div>
  <div class="folio" style="left:8px">07</div>
</section>

<section class="page dark team" style="left:330px;top:446px">
  <div class="portrait" role="img" aria-label="Portrait photo of Fahad Rashed" style="left:110px;top:66px;width:22px;height:22px"></div>
  <div class="portrait" role="img" aria-label="Portrait photo of Tarek Mansour" style="left:146px;top:66px;width:22px;height:22px"></div>
  <div class="fine on-dark" style="left:62px;top:92px;width:72px;text-align:center"><b>FAHAD RASHED</b>Projects Manager<br><br>Certified project lead with deep skill in HR systems, payroll and large scale rollout for public and private firms.</div>
  <div class="fine on-dark" style="left:146px;top:92px;width:70px"><b>TAREK MANSOUR</b>Consultant<br><br>Skilled in training design, coaching and review of people and roles for fast growing teams.</div>
  <div class="folio" style="right:8px">08</div>
</section>

<section class="page certs" style="left:605px;top:446px">
  <div class="panel" style="left:0;top:0;width:100%;height:100px;background:var(--panel-light)"></div>
  <div class="title" style="left:19px;top:78px;font-size:12px;font-weight:700">CERTIFICATIONS</div>
  <div class="logo-grid" style="left:19px;top:106px;width:230px;height:68px;grid-template-columns:repeat(4,1fr);grid-template-rows:repeat(3,1fr);font-size:4.8px">
    <div class="logo-cell"><span class="sq"></span>Marlow Assess</div>
    <div class="logo-cell"><span class="sq"></span>Brightpath</div>
    <div class="logo-cell"><span class="sq"></span>Wellform</div>
    <div class="logo-cell"><span class="sq"></span>Modulo</div>
    <div class="logo-cell"><span class="sq"></span>Halden Guild</div>
    <div class="logo-cell"><span class="sq"></span>Psych Board</div>
    <div class="logo-cell"><span class="sq"></span>Quentra</div>
    <div class="logo-cell"><span class="sq"></span>Ferris</div>
    <div class="logo-cell"><span class="sq"></span>Kestrel</div>
    <div class="logo-cell"><span class="sq"></span>Ravel Coaching</div>
    <div class="logo-cell"><span class="sq"></span>Talvo</div>
    <div class="logo-cell"><span class="sq"></span>Orvena</div>
  </div>
  <div class="folio" style="left:8px">09</div>
</section>

<section class="page clients" style="left:879px;top:446px">
  <div class="panel" style="left:0;top:0;width:100%;height:100px;background:var(--panel-light)"></div>
  <div class="title" style="left:22px;top:78px;font-size:12px;font-weight:700">OUR CLIENTS</div>
  <div class="logo-grid" style="left:22px;top:106px;width:226px;height:66px;grid-template-columns:repeat(4,1fr);grid-template-rows:repeat(2,1fr);font-size:4.8px">
    <div class="logo-cell"><span class="sq"></span>Civic Care Fund</div>
    <div class="logo-cell"><span class="sq"></span>Northway</div>
    <div class="logo-cell"><span class="sq"></span>Eduvia</div>
    <div class="logo-cell"><span class="sq"></span>Harbor Auth.</div>
    <div class="logo-cell"><span class="sq"></span>Velchem</div>
    <div class="logo-cell"><span class="sq"></span>Nazeer Inv.</div>
    <div class="logo-cell"><span class="sq"></span>Netlyn</div>
    <div class="logo-cell"><span class="sq"></span>Coastline</div>
  </div>
  <div class="folio" style="right:8px">10</div>
</section>

</body>
</html>
```